NZ First of it's kind solutions directory and marketplace for busy Mums needs a business card design

We need a business card design for our new nationwide business in NZ (long term plans to go global). We provide solutions to the everyday challenges that busy Mums face by connecting them with quality communities and suppliers of carefully selected, relevant products and services. We sell direct via our online marketplace. The final design should communicate our values of inclusivity, quality and smart solutions. Colours should incorporate our logo colour palette of #477077 and #6ba8b2. Our website is at https://www.brightnestly.com

Target Market(s)

busy Mums, Age 28 – 50, female, income over $100K, location main centres NZ primarily but NZ wide. Is likely juggling work or career with a young family. Probably had hobbies which have fallen by the wayside.
-Wants to succeed in her chosen career without compromising on family life
-to successfully juggle her career without feeling like she is compromising her children
- Is time poor, something always has to give and it’s generally her health (she’ll stay up late, get stressed)
- probably ex corporate or professional career. Has discretional income

Industry/Entity Type

Business

Contact Information for Business Card

Jodie Farnsworth, Founder, BrightNestly.com (Strapline Browse; Pick; Sorted), 48 Kowhai Terrace, Hillsborough, Auckland 1058, New Zealand. Mob: 021 437 518 Ph: +64 (0)9 584 7163

Font styles to use
Other font styles liked:
• Raleway, and/or Architects Daughter

Colors
00a990
33b8a4
86cfc6
cfeae6

Requirements
Must have
• the above details, streamline. the logo and colours associated with those logos
Should not have
• foil or metallic colours

```html
<!DOCTYPE html>
<html lang="en">
<head>
<meta charset="utf-8">
<title>BrightNestly Business Card</title>
<link href="https://fonts.googleapis.com/css2?family=Roboto+Condensed:wght@700&family=Roboto:wght@400;500&display=swap" rel="stylesheet">
<style>
  :root {
    --brand-dark: #477077;
    --brand-panel: #4a7277;
    --brand-light: #6ba8b2;
    --back-fill: #6aa7b1;
    --paper: #f1f1f1;
    --white: #ffffff;
    --stage: #2b2b2b;
  }
  * { margin: 0; padding: 0; box-sizing: border-box; }
  html, body { width: 1200px; height: 960px; overflow: hidden; }
  body {
    position: relative;
    background: var(--stage);
    font-family: "Roboto", Arial, sans-serif;
    color: var(--white);
  }
  .card {
    position: absolute;
    width: 600px;
    height: 343px;
    overflow: hidden;
    box-shadow: 0 3px 6px rgba(0,0,0,0.45);
  }
  .card-front { left: 314px; top: 113px; background: var(--brand-panel); }
  .card-back { left: 311px; top: 472px; background: var(--back-fill); }

  .front-curve { position: absolute; inset: 0; }

  .brand-lockup {
    position: absolute;
    left: 287px;
    top: 80px;
    display: flex;
    align-items: center;
    gap: 12px;
  }
  .brand-dot {
    width: 30px; height: 30px;
    border-radius: 50%;
    background: var(--brand-dark);
  }
  .brand-name {
    font-family: "Roboto", Arial, sans-serif;
    font-weight: 500;
    font-size: 34px;
    color: var(--brand-dark);
    letter-spacing: -0.5px;
  }

  .contact { position: absolute; left: 32px; top: 154px; }
  .contact-name {
    font-family: "Roboto Condensed", "Arial Narrow", sans-serif;
    font-weight: 700;
    font-size: 22px;
    line-height: 26px;
    text-transform: uppercase;
  }
  .contact-role {
    font-size: 15px;
    line-height: 20px;
    text-transform: uppercase;
    margin-bottom: 14px;
  }
  .contact-address { font-size: 14.5px; line-height: 19px; margin-bottom: 10px; }
  .contact-list { list-style: none; font-size: 14.5px; line-height: 19px; }
  .contact-list li { display: flex; align-items: center; gap: 8px; }
  .contact-list svg { width: 14px; height: 14px; flex: none; fill: var(--white); }

  .back-lockup {
    position: absolute;
    left: 0; right: 0; top: 140px;
    display: flex;
    justify-content: center;
    align-items: center;
    gap: 16px;
  }
  .back-dot { width: 44px; height: 44px; border-radius: 50%; background: var(--white); }
  .back-name {
    font-family: "Roboto", Arial, sans-serif;
    font-weight: 500;
    font-size: 52px;
    color: var(--white);
  }
  .tagline {
    position: absolute;
    left: 0; right: 0; top: 305px;
    text-align: center;
    font-size: 14.5px;
  }
</style>
</head>
<body>

<section class="card card-front">
  <svg class="front-curve" viewBox="0 0 600 343" width="600" height="343" aria-hidden="true">
    <path d="M316 0 C190 45 196 228 396 343 L600 343 L600 0 Z" fill="var(--brand-light)"/>
    <path d="M324 0 C202 44 206 226 402 343" fill="none" stroke="var(--white)" stroke-width="2"/>
    <path d="M334 0 C218 44 218 224 408 343 L600 343 L600 0 Z" fill="var(--paper)"/>
  </svg>

  <div class="brand-lockup">
    <span class="brand-dot"></span>
    <span class="brand-name">BrightNestly</span>
  </div>

  <div class="contact">
    <h1 class="contact-name">Jodie Farnsworth</h1>
    <p class="contact-role">Founder</p>
    <p class="contact-address">48 Kowhai Terrace, Hillsborough<br>Auckland 1058, New Zealand.</p>
    <ul class="contact-list">
      <li>
        <svg viewBox="0 0 16 16"><path d="M3.6 1.2l2.3 2.4-1.2 1.8c.8 1.9 2.2 3.3 4.1 4.1l1.8-1.2 2.4 2.3-1.5 2.3C6.4 12.7 3.3 9.6 1.2 4.5z"/></svg>
        +64 (0)9 584 7163
      </li>
      <li>
        <svg viewBox="0 0 16 16"><path d="M4 1h8v14H4zM5.5 2.5v9.5h5V2.5zM7.3 13h1.4v1H7.3z" fill-rule="evenodd"/></svg>
        021 437 518
      </li>
      <li>
        <svg viewBox="0 0 16 16"><circle cx="8" cy="8" r="7"/><path d="M4 5c2 0 2 2 4 2s1 3-1 3-1 3-2 3M10 2c0 2 2 2 3 3" fill="none" stroke="var(--brand-panel)" stroke-width="1.4"/></svg>
        BrightNestly.com
      </li>
    </ul>
  </div>
</section>

<section class="card card-back">
  <div class="back-lockup">
    <span class="back-dot"></span>
    <span class="back-name">BrightNestly</span>
  </div>
  <p class="tagline">Browse; Pick; Sorted</p>
</section>

</body>
</html>
```